Enchilada sauce needs bright,delicious,appealing, attention-grabbing label

We are Copperfield Hearth LLC., and we need a label for a 20 oz. round jar w/ gold or black lid containing a most delicious and very hard to find Enchilada Sauce. The sauce itself is a deep, rich, dark red sauce in a glass container. The colors of the label should be the colors of sunset but also a pop of bright blue, yellow, white and black, maybe white letters for the name, which is MOLTA and underneath, (enchilada salsa para muchos usos)

Your design will be on supermarket shelves across the USA and hopefully beyond, depends on how clever you are.                                   

should have chili peppers represented

```html
<!DOCTYPE html>
<html lang="en">
<head>
<meta charset="utf-8">
<title>MOLTA Enchilada Sauce Label</title>
<link rel="stylesheet" href="https://fonts.googleapis.com/css2?family=Great+Vibes&family=Vollkorn+SC:wght@400&family=Encode+Sans+Condensed:wght@300&family=Kaushan+Script&family=Roboto:wght@400&display=swap">
<style>
  :root {
    --bg: #ffffff;
    --label-red: #e0232c;
    --label-red-light: #ec2b25;
    --ring-red: #d8232e;
    --ring-green: #8a9b3a;
    --ring-yellow: #f3ea22;
    --white: #ffffff;
    --accent-yellow: #f6ec2a;
    --gold-light: #f3e07a;
    --gold-mid: #d9b24a;
    --gold-dark: #9a6a22;
    --ribbon-text: #d8232e;
  }
  html, body {
    margin: 0;
    padding: 0;
    width: 1200px;
    height: 1000px;
    overflow: hidden;
    background: var(--bg);
  }
  .label-canvas { display: block; width: 1200px; height: 1000px; }
  .tagline-script { font-family: "Great Vibes", cursive; font-size: 34px; fill: var(--accent-yellow); }
  .brand-name { font-family: "Vollkorn SC", serif; font-size: 112px; fill: var(--white); letter-spacing: 3px; }
  .trademark { font-family: "Encode Sans Condensed", sans-serif; font-size: 20px; fill: var(--white); }
  .subtitle { font-family: "Encode Sans Condensed", sans-serif; font-weight: 300; font-size: 25px; fill: var(--accent-yellow); letter-spacing: 0.5px; }
  .maker-name { font-family: "Kaushan Script", cursive; font-size: 26px; fill: var(--ribbon-text); }
  .net-weight { font-family: "Roboto", sans-serif; font-size: 16px; fill: var(--white); }
</style>
</head>
<body>
<svg class="label-canvas" viewBox="0 0 1200 1000" xmlns="http://www.w3.org/2000/svg">
  <defs>
    <linearGradient id="label-fill" x1="0" x2="1" y1="0" y2="0">
      <stop offset="0" stop-color="var(--label-red)"/>
      <stop offset="0.5" stop-color="var(--label-red-light)"/>
      <stop offset="1" stop-color="var(--label-red)"/>
    </linearGradient>
    <linearGradient id="gold-band" x1="0" x2="1" y1="0" y2="0">
      <stop offset="0" stop-color="var(--gold-dark)"/>
      <stop offset="0.3" stop-color="var(--gold-light)"/>
      <stop offset="0.7" stop-color="var(--gold-light)"/>
      <stop offset="1" stop-color="var(--gold-dark)"/>
    </linearGradient>
    <linearGradient id="pepper-fill" x1="0" x2="0" y1="0" y2="1">
      <stop offset="0" stop-color="#e8432a"/>
      <stop offset="1" stop-color="#c41f26"/>
    </linearGradient>
    <path id="ribbon-arc" d="M445 605 Q600 570 755 605"/>
  </defs>

  <g class="label-rings">
    <ellipse cx="600" cy="501" rx="306" ry="334" fill="var(--ring-red)"/>
    <ellipse cx="600" cy="501" rx="302" ry="330" fill="var(--ring-green)"/>
    <ellipse cx="600" cy="501" rx="295" ry="323" fill="var(--ring-yellow)"/>
    <ellipse cx="600" cy="501" rx="288" ry="316" fill="var(--ring-green)"/>
    <ellipse cx="600" cy="501" rx="285" ry="313" fill="var(--ring-yellow)"/>
    <ellipse cx="600" cy="501" rx="280" ry="308" fill="var(--ring-red)"/>
    <ellipse cx="600" cy="501" rx="276" ry="304" fill="var(--white)"/>
    <ellipse cx="600" cy="501" rx="271" ry="299" fill="url(#label-fill)"/>
  </g>

  <g class="tagline-flag">
    <polygon points="422,298 460,298 460,341 422,341 434,320" fill="var(--accent-yellow)"/>
    <polygon points="740,298 778,298 766,320 778,341 740,341" fill="var(--accent-yellow)"/>
    <text class="tagline-script" x="600" y="332" text-anchor="middle">Enchilada Sauce</text>
  </g>

  <g class="divider-rules" stroke="var(--accent-yellow)" stroke-width="2" fill="var(--accent-yellow)">
    <line x1="378" y1="365" x2="826" y2="365"/>
    <circle cx="376" cy="365" r="3"/>
    <circle cx="828" cy="365" r="3"/>
    <line x1="378" y1="493" x2="826" y2="493"/>
    <circle cx="376" cy="493" r="3"/>
    <circle cx="828" cy="493" r="3"/>
  </g>

  <text class="brand-name" x="586" y="468" text-anchor="middle">Molta</text>
  <text class="trademark" x="778" y="408">TM</text>

  <text class="subtitle" x="600" y="531" text-anchor="middle">ENCHILADA SALSA PARA MUCHOS USOS</text>

  <g class="maker-ribbon">
    <polygon points="398,605 440,590 444,640 402,655 416,628" fill="var(--gold-mid)"/>
    <polygon points="802,605 760,590 756,640 798,655 784,628" fill="var(--gold-mid)"/>
    <path d="M428 585 Q600 548 772 585 L772 632 Q600 595 428 632 Z" fill="url(#gold-band)"/>
    <text class="maker-name" text-anchor="middle"><textPath href="#ribbon-arc" startOffset="50%">Copperfield Hearth LLC.</textPath></text>
  </g>

  <rect class="pepper-illustration" x="512" y="636" width="176" height="98" rx="40" fill="url(#pepper-fill)" role="img" aria-label="Two crossed red chili peppers with a small flame between them"/>

  <text class="net-weight" x="600" y="769" text-anchor="middle">Net wt. 20oz.</text>
</svg>
</body>
</html>
```